Event flyer for Sunday night Youth Group

Need a 4 x 6 or 5 x 7 flyer for a new youth group starting on April 14. The youth group is for students in middle school and high school so it needs to look fun and cool, but not childish. I prefer it not to include pictures of people unless it's so obscure you can't really see their faces. I've uploaded some pictures of flyers I like. I've also attached a couple versions of our logo to use on the flyer.
Information the flyer needs to include:
Youth Group
Sundays, 6-8pm (beginning April 14)
Location: Merriwick's - 4219 Hollowfern Ln S, Keizer, 97418
There will be dinner, games, friends, and a message.
Target Market(s)
Youth ages 13-18
Industry/Entity Type
Church
Colors
Designer to choose colors to be used in the design.
Look and feel

```html
<!DOCTYPE html>
<html lang="en">
<head>
<meta charset="utf-8">
<title>Youth Group Flyer</title>
<link rel="stylesheet" href="https://fonts.googleapis.com/css2?family=Bungee&family=Oswald:wght@600&family=Open+Sans:wght@400;700&family=Archivo+Black&display=swap">
<style>
  :root {
    --stage: #d3cbc6;
    --night: #2a2566;
    --glow-hi: #fff3b0;
    --glow-mid: #f7a428;
    --glow-low: #c8451c;
    --ember: #6a2418;
    --sky-blue: #29abe2;
    --deep-blue: #2b2466;
    --paper: #ffffff;
  }
  * { margin: 0; padding: 0; box-sizing: border-box; }
  html, body { width: 1200px; height: 1024px; overflow: hidden; }
  body { background: var(--stage); position: relative; font-family: "Open Sans", sans-serif; }

  .flyer {
    position: absolute; left: 267px; top: 41px;
    width: 665px; height: 941px; overflow: hidden;
    background: var(--night);
  }
  .flyer__backdrop {
    position: absolute; inset: 0;
    background:
      radial-gradient(ellipse 60% 28% at 70% 10%, var(--glow-hi), rgba(255,243,176,0) 70%),
      linear-gradient(180deg, var(--glow-mid) 0%, #e9801f 22%, var(--glow-low) 42%, var(--ember) 58%, var(--night) 76%, var(--night) 100%);
  }
  .flyer__content { position: absolute; inset: 0; text-align: center; color: var(--paper); }

  .title-youth {
    position: absolute; left: 0; right: 0; top: 158px;
    font-family: "Bungee", sans-serif; font-size: 140px; line-height: 1;
    color: var(--sky-blue);
    text-shadow: 3px 3px 0 var(--paper), 9px 9px 0 var(--deep-blue), 12px 12px 0 var(--deep-blue);
    transform: scaleY(1.45) rotate(-2deg); transform-origin: top center;
    letter-spacing: -4px;
  }
  .title-group {
    position: absolute; left: 0; right: 0; top: 360px;
    font-family: "Oswald", sans-serif; font-weight: 600; font-size: 118px; line-height: 1;
  }
  .schedule {
    position: absolute; left: 0; right: 0; top: 536px;
    font-weight: 700; font-size: 24px; line-height: 1.3;
  }
  .schedule__start { font-weight: 400; font-size: 20px; }
  .venue-name {
    position: absolute; left: 0; right: 0; top: 612px;
    font-weight: 700; font-size: 33px;
  }
  .venue-address {
    position: absolute; left: 0; right: 0; top: 657px;
    font-size: 23px;
  }
  .tagline {
    position: absolute; left: 0; right: 0; top: 757px;
    font-size: 22px; letter-spacing: -0.3px;
  }
  .tagline__accent {
    font-family: "Archivo Black", sans-serif; font-size: 21px; letter-spacing: 2.5px; margin-left: 6px;
  }
  .church-name {
    position: absolute; left: 0; right: 0; top: 818px;
    display: flex; justify-content: center; align-items: center; gap: 16px;
    font-size: 30px; font-weight: 400; letter-spacing: 1px;
  }
  .church-name__mark { width: 34px; height: 34px; background: var(--paper); }
</style>
</head>
<body>
  <main class="flyer">
    <div class="flyer__backdrop" role="img" aria-label="Blurred concert crowd under warm orange stage lights fading into deep navy"></div>
    <div class="flyer__content">
      <h1 class="title-youth">YOUTH</h1>
      <p class="title-group">Group</p>
      <p class="schedule">Sundays, 6-8pm <span class="schedule__start">(beginning April 14)</span></p>
      <p class="venue-name">Merriwick's</p>
      <p class="venue-address">4219 Hollowfern Ln S Keizer, 97418</p>
      <p class="tagline">There will be dinner, games, friends, and <span class="tagline__accent">a message</span></p>
      <div class="church-name"><span class="church-name__mark"></span><span>Wayfield Fellowship</span></div>
    </div>
  </main>
</body>
</html>
```